FAST TURN AROUND - Yoga & Sound Meditation Event Flyer

Our organization - Corvid Stewardship Circle - is currently looking for someone to create a flyer for an upcoming Yoga & Sound Meditation Event.

We are looking for the following deliverables:
Versions of the Flyer created for Social Media (Long Story & Square Post) that includes the following information. (Not including the categories)
Event Title: Corvid Sway & Hum Wind Down Edition - Lunaport Mixdown
Event Date & Time: Wednesday, April 20 | 7P - 9P
Event Location: Pebblehall at Fernway
Corvid Logo: (Both black and white versions are attached. Feel free to use whichever makes more sense based on the lighting)

We would want a version of this for the eight different background images provided. For the test, you can submit 1-2 since the rest of the details will be the same once we chose the information design.

```html
<!DOCTYPE html>
<html lang="en">
<head>
<meta charset="utf-8">
<title>Corvid Sway &amp; Hum — Wind Down Edition posts</title>
<link rel="stylesheet" href="https://fonts.googleapis.com/css2?family=Allura&family=Jost:wght@400;700&family=Oswald:wght@500&display=swap">
<style>
  :root {
    --page: #ffffff;
    --paper: #e9e2e0;
    --tan: #d39a6a;
    --plum: #6a2150;
    --plum-band: #62234d;
    --ink: #2e2f45;
    --white: #ffffff;
  }
  * { box-sizing: border-box; margin: 0; padding: 0; }
  html, body { width: 1200px; height: 960px; overflow: hidden; background: var(--page); }
  .board { position: relative; width: 1200px; height: 960px; }
  .post {
    position: absolute; top: 303px; width: 353px; height: 353px;
    background: var(--paper); overflow: hidden;
  }
  .post--one { left: 39px; }
  .post--two { left: 422px; }
  .post--three { left: 802px; }

  .brush { position: absolute; display: block; z-index: 2; }
  .brush--top { left: 0; top: 0; width: 353px; height: 40px; }
  .brush--corner { right: 0; bottom: 0; width: 120px; height: 46px; z-index: 1; }

  .photo {
    position: absolute; left: 0; top: 12px; width: 353px; height: 215px; z-index: 1;
    -webkit-mask-image: linear-gradient(to bottom, #000 65%, transparent 100%);
    mask-image: linear-gradient(to bottom, #000 65%, transparent 100%);
  }
  .photo--gong { background: linear-gradient(120deg, #6f625c 0%, #d9d2cf 35%, #c59c80 60%, #efeae8 100%); }
  .photo--candles { background: linear-gradient(110deg, #d8d2cd 0%, #f3efe9 30%, #3a2a24 52%, #d48c4f 68%, #9aa0a4 100%); }
  .photo--circle { background: radial-gradient(circle at 50% 40%, #e88a2a 0%, #a04e14 35%, #3b1e0e 75%, #231308 100%); }

  .title-script, .title-main, .subtitle, .details, .brand, .dots { z-index: 3; }
  .title-script {
    position: absolute; left: 0; width: 353px; top: 204px;
    text-align: center; font-family: "Allura", cursive; white-space: nowrap;
    font-size: 46px; line-height: 1; color: var(--plum);
  }
  .title-main {
    position: absolute; left: 0; width: 353px; top: 250px;
    text-align: center; font-family: "Jost", sans-serif; font-weight: 400; white-space: nowrap;
    font-size: 26px; line-height: 1; color: var(--ink); letter-spacing: 0.2px;
  }
  .dots {
    position: absolute; top: 259px; width: 3px; height: 13px;
    background: radial-gradient(circle, var(--plum) 1.2px, transparent 1.5px) 0 0 / 3px 5px repeat-y;
  }
  .dots--left { left: 21px; }
  .dots--right { right: 18px; }
  .subtitle {
    position: absolute; left: 0; width: 353px; top: 279px;
    text-align: center; font-family: "Jost", sans-serif; font-weight: 400; white-space: nowrap;
    font-size: 11.5px; line-height: 1; color: var(--ink);
  }
  .details {
    position: absolute; left: 0; top: 295px; width: 353px; height: 12px;
    background: var(--plum-band); color: var(--white); white-space: nowrap;
    font-family: "Oswald", sans-serif; font-weight: 500; font-size: 6.6px;
    letter-spacing: 0.9px; line-height: 12px; text-align: center; text-transform: uppercase;
  }
  .brand {
    position: absolute; left: 0; width: 353px; top: 316px; text-align: center;
    color: var(--ink); font-family: "Jost", sans-serif;
  }
  .brand-name { display: block; font-weight: 700; font-size: 19px; line-height: 1; }
  .brand-tag { display: block; font-weight: 400; font-size: 6.5px; line-height: 1.3; margin-top: 1px; }
</style>
</head>
<body>
<main class="board">

  <article class="post post--one">
    <svg class="brush brush--top" viewBox="0 0 353 40" aria-hidden="true"><path d="M0 0H175L168 4L182 2L150 14L120 20L80 24L30 27L0 32Z" fill="var(--tan)"/></svg>
    <div class="photo photo--gong" role="img" aria-label="Photo: sound healer playing a gong, eyes closed"></div>
    <p class="title-script">Corvid sway &amp; hum</p>
    <span class="dots dots--left"></span>
    <h1 class="title-main">WIND DOWN EDITION</h1>
    <span class="dots dots--right"></span>
    <p class="subtitle">LUNAPORT MIXDOWN</p>
    <p class="details">Wednesday, April 20 &nbsp;|&nbsp; 7PM - 9PM at Pebblehall at Fernway</p>
    <div class="brand"><span class="brand-name">corvid.</span><span class="brand-tag">Corvid Stewardship Circle</span></div>
    <svg class="brush brush--corner" viewBox="0 0 120 46" aria-hidden="true"><path d="M0 0H85L60 20L45 26L70 14L95 0H120V46H100L95 30L80 10L78 46H70L40 28L20 12Z" fill="var(--tan)"/></svg>
  </article>

  <article class="post post--two">
    <svg class="brush brush--top" viewBox="0 0 353 40" aria-hidden="true"><path d="M0 0H175L168 4L182 2L150 14L120 20L80 24L30 27L0 32Z" fill="var(--tan)"/></svg>
    <div class="photo photo--candles" role="img" aria-label="Photo: woman in an orange wrap seated beside a candlelit table with singing bowls"></div>
    <p class="title-script">Corvid sway &amp; hum</p>
    <span class="dots dots--left"></span>
    <h1 class="title-main">WIND DOWN EDITION</h1>
    <span class="dots dots--right"></span>
    <p class="subtitle">LUNAPORT MIXDOWN</p>
    <p class="details">Wednesday, April 20 &nbsp;|&nbsp; 7PM - 9PM at Pebblehall at Fernway</p>
    <div class="brand"><span class="brand-name">corvid.</span><span class="brand-tag">Corvid Stewardship Circle</span></div>
    <svg class="brush brush--corner" viewBox="0 0 120 46" aria-hidden="true"><path d="M0 0H85L60 20L45 26L70 14L95 0H120V46H100L95 30L80 10L78 46H70L40 28L20 12Z" fill="var(--tan)"/></svg>
  </article>

  <article class="post post--three">
    <svg class="brush brush--top" viewBox="0 0 353 40" aria-hidden="true"><path d="M0 0H175L168 4L182 2L150 14L120 20L80 24L30 27L0 32Z" fill="var(--tan)"/></svg>
    <div class="photo photo--circle" role="img" aria-label="Photo: gong player silhouetted in a warm amber-lit room with resting participants"></div>
    <p class="title-script">Corvid sway &amp; hum</p>
    <span class="dots dots--left"></span>
    <h1 class="title-main">WIND DOWN EDITION</h1>
    <span class="dots dots--right"></span>
    <p class="subtitle">LUNAPORT MIXDOWN</p>
    <p class="details">Wednesday, April 20 &nbsp;|&nbsp; 7PM - 9PM at Pebblehall at Fernway</p>
    <div class="brand"><span class="brand-name">corvid.</span><span class="brand-tag">Corvid Stewardship Circle</span></div>
    <svg class="brush brush--corner" viewBox="0 0 120 46" aria-hidden="true"><path d="M0 0H85L60 20L45 26L70 14L95 0H120V46H100L95 30L80 10L78 46H70L40 28L20 12Z" fill="var(--tan)"/></svg>
  </article>

</main>
</body>
</html>
```